Shampoo and Shower Gel Packaging Design

I need a new packaging design for a men shampoo and shower gel bottle. The packaging must me black (black bottle/package) and the logo should be also monochrom.
For example, black matte bottle and black shiny logo on the packaging (not mandatory).
the design must contain maximum 3 colors.
1. black
2. white (text)
3. grey/dark blue/dark green (colors will be the difference between products parfumes/smell/scences.

Design must be minimalist/elegant/discrete.
Updates

Please check the photos i added for pure inspiration.

Target Market(s)

brand exclusively for MEN - premium clients

Industry/Entity Type

Cosmetics

Font styles to use
Sans Serif

Colors
1b1b1b
5c5c5c
aaaaaa
ffffff
3176b5

Requirements
Must have
• black background
• minimalist design

```html
<!DOCTYPE html>
<html lang="en">
<head>
<meta charset="utf-8">
<title>Varro Shower Gel – Bergamot Label</title>
<link rel="stylesheet" href="https://fonts.googleapis.com/css2?family=Josefin+Sans:wght@300&family=Lato:wght@400;700&display=swap">
<style>
  :root {
    --label-black: #111314;
    --ring-grey: #a9b1b3;
    --text-white: #ffffff;
    --scent-olive: #a8a83a;
    --volume-grey: #9aa3a5;
  }
  html, body {
    margin: 0;
    padding: 0;
    width: 1200px;
    height: 1200px;
    overflow: hidden;
    background: var(--label-black);
  }
  .label {
    position: relative;
    width: 1200px;
    height: 1200px;
    background: var(--label-black);
  }
  .seal {
    position: absolute;
    left: 0;
    top: 0;
    width: 1200px;
    height: 1200px;
  }
  .seal__ring { fill: none; stroke: var(--ring-grey); }
  .seal__ring--outer { stroke-width: 8; }
  .seal__ring--inner { stroke-width: 5; }
  .seal__product {
    font-family: "Lato", sans-serif;
    font-weight: 400;
    font-size: 44px;
    letter-spacing: 19px;
    fill: var(--text-white);
  }
  .seal__scent {
    font-family: "Lato", sans-serif;
    font-weight: 400;
    font-size: 50px;
    letter-spacing: 22px;
    fill: var(--scent-olive);
  }
  .brand__dot { fill: var(--text-white); }
  .brand__name,
  .brand__tagline {
    font-family: "Josefin Sans", sans-serif;
    font-weight: 300;
    fill: var(--text-white);
  }
  .brand__name { font-size: 66px; letter-spacing: 26px; }
  .brand__tagline { font-size: 15px; letter-spacing: 7px; }
  .volume {
    position: absolute;
    left: 0;
    width: 1200px;
    top: 926px;
    margin: 0;
    text-align: center;
    font-family: "Lato", sans-serif;
    font-weight: 700;
    font-size: 30px;
    letter-spacing: 6px;
    color: var(--volume-grey);
  }
</style>
</head>
<body>
  <main class="label">
    <svg class="seal" viewBox="0 0 1200 1200" xmlns="http://www.w3.org/2000/svg">
      <defs>
        <path id="arc-top" d="M 382 505 A 218 218 0 0 1 818 505"/>
        <path id="arc-bottom" d="M 372 505 A 228 228 0 0 0 828 505"/>
      </defs>

      <circle class="seal__ring seal__ring--outer" cx="601" cy="508" r="272"/>
      <circle class="seal__ring seal__ring--inner" cx="601" cy="501" r="190"/>

      <text class="seal__product">
        <textPath href="#arc-top" startOffset="50%" text-anchor="middle">SHOWER GEL</textPath>
      </text>
      <text class="seal__scent">
        <textPath href="#arc-bottom" startOffset="50%" text-anchor="middle">bergamot</textPath>
      </text>

      <g class="brand">
        <circle class="brand__dot" cx="600" cy="455" r="10"/>
        <text class="brand__name" x="613" y="560" text-anchor="middle">VARRO</text>
        <text class="brand__tagline" x="603" y="591" text-anchor="middle">COSMETICS</text>
      </g>
    </svg>

    <p class="volume">4 FL. OZ.</p>
  </main>
</body>
</html>
```